Online-Marketing-Material für Autor
Hallo,
ich benötige für ein bereits fertiges Cover noch einige Grafiken um das Buch auf SociaMedia zu bewerben.
Nachdem es sich um einen Erotikroman handelt, geschrieben aus der Sicht eines Mannes, gehe ich davon aus, das das hauptsächlich Männer interessieren wird.
Es handelt sich um folgenden Roman: https://www.buchladenvoll.de/dp/K7TRWMXZQD
Aufgabenstellung
Die benötigten Grafiken im einzelnen:
* Hochformat: 660 x 1173 Pixel
* Quadratisch: 1080 Pixel
* Querformat: 1173 x 660 Pixel
Die Bilder sollten beinhalten:
* Das Cover
* Der Text 'Jetzt im Handel' und 'Zum Einführungspreis von xx%'
* Die Beschreibung des Buches sollte gut lesbar vorkommen:
Eines Tages kauft der Student Roman ein neuartiges Online-Computerspiel und weiß zu diesem Zeitpunkt noch nicht, dass sich sein Sex-Leben dadurch drastisch verbessern wird.

```html
<!DOCTYPE html>
<html lang="de">
<head>
<meta charset="utf-8">
<title>Sex auf Velora – Anfangsgebiet</title>
<link rel="stylesheet" href="https://fonts.googleapis.com/css2?family=Arimo:wght@400;700&display=swap">
<style>
  :root {
    --mist-light: #e4ecee;
    --mist-mid: #9fbcc4;
    --forest-dark: #3f5a62;
    --figure-tone: #7d7a78;
    --figure-skin: #c9b4a6;
    --price-panel: rgba(78, 82, 84, 0.78);
    --badge-fill: #6aa9bd;
    --badge-ring: #1c2326;
    --ink: #111111;
    --white: #ffffff;
    --device-frame: #1d1f21;
  }
  * { margin: 0; padding: 0; box-sizing: border-box; }
  html, body { width: 1200px; height: 675px; overflow: hidden; background: var(--mist-light); }
  .promo {
    position: relative;
    width: 1200px;
    height: 675px;
    overflow: hidden;
    font-family: "Arimo", Arial, sans-serif;
  }
  .forest-backdrop {
    position: absolute; inset: 0;
    background:
      linear-gradient(180deg, rgba(255,255,255,0) 50%, rgba(240,245,246,0.95) 85%),
      linear-gradient(90deg, var(--forest-dark) 0%, var(--mist-mid) 40%, #a9c9d0 60%, var(--forest-dark) 100%);
  }
  .heroine-art {
    position: absolute; left: 0; top: 0; width: 560px; height: 675px;
    background:
      radial-gradient(ellipse 120px 200px at 290px 330px, var(--figure-skin) 0%, rgba(201,180,166,0) 100%),
      linear-gradient(90deg, rgba(60,62,64,0.9) 0%, var(--figure-tone) 45%, rgba(125,122,120,0) 100%);
  }
  .title-band {
    position: absolute; left: 0; top: 400px; width: 620px; height: 240px;
    background: linear-gradient(90deg, rgba(40,42,44,0.55), rgba(40,42,44,0.15) 80%, rgba(40,42,44,0));
    border-radius: 0 200px 0 0;
  }
  .book-title {
    position: absolute; left: 100px; top: 440px; width: 380px;
    color: var(--white);
    font-weight: 700;
  }
  .book-title .title-name { font-size: 56px; line-height: 1.05; }
  .book-title .title-sub { margin-top: 14px; font-size: 30px; line-height: 1.1; }
  .price-panel {
    position: absolute; left: 631px; top: 75px; width: 300px; height: 160px;
    background: var(--price-panel);
    border-radius: 10px 0 0 0;
    color: var(--white);
    padding: 14px 0 0 28px;
    font-size: 27.5px; line-height: 1.15;
  }
  .price-panel .price { font-weight: 700; font-size: 56px; margin-left: 6px; line-height: 1; }
  .price-panel .currency { font-weight: 700; font-size: 24px; vertical-align: 26px; }
  .sale-badge {
    position: absolute; left: 551px; top: 195px; width: 160px; height: 160px;
    border-radius: 50%;
    background: var(--badge-fill);
    border: 3px solid var(--badge-ring);
    display: flex; align-items: center; justify-content: center;
    text-align: center;
  }
  .sale-badge span {
    transform: rotate(-8deg);
    font-weight: 700; font-size: 30px; line-height: 1.3; color: var(--ink);
  }
  .device { position: absolute; background: var(--device-frame); box-shadow: 0 6px 14px rgba(0,0,0,0.35); }
  .device-tablet { left: 922px; top: 68px; width: 248px; height: 327px; border-radius: 16px; padding: 10px; }
  .device-phone { left: 858px; top: 176px; width: 108px; height: 219px; border-radius: 16px; padding: 6px; }
  .device-screen {
    position: relative; width: 100%; height: 100%; border-radius: 8px; overflow: hidden;
    background:
      radial-gradient(ellipse 40% 30% at 50% 45%, var(--figure-skin), rgba(201,180,166,0)),
      linear-gradient(180deg, #6f8a90, var(--figure-tone) 60%, #4a4c4e);
    color: var(--white); text-align: center;
  }
  .device-screen .cover-author { position: absolute; top: 6px; width: 100%; }
  .device-screen .cover-title { position: absolute; width: 100%; font-weight: 700; line-height: 1.1; }
  .device-tablet .cover-author { font-size: 10px; }
  .device-tablet .cover-title { top: 190px; font-size: 22px; }
  .device-tablet .cover-sub { display: block; font-size: 12px; margin-top: 4px; }
  .device-phone .cover-author { font-size: 5px; top: 16px; }
  .device-phone .cover-title { top: 112px; font-size: 10px; }
  .device-phone .cover-sub { display: block; font-size: 6px; margin-top: 2px; }
  .device-phone .cover-genre { position: absolute; bottom: 22px; width: 100%; font-weight: 700; font-size: 5px; }
  .book-pitch { position: absolute; left: 631px; top: 428px; width: 538px; color: var(--ink); }
  .book-pitch h1 {
    font-weight: 700; font-size: 27.5px; line-height: 1.17; text-transform: uppercase;
  }
  .book-pitch p { margin-top: 6px; font-size: 26px; line-height: 1.16; }
  .book-pitch .line { display: block; text-align: justify; text-align-last: justify; white-space: nowrap; }
  .book-pitch .line-last { display: block; }
</style>
</head>
<body>
<main class="promo">
  <div class="forest-backdrop" role="img" aria-label="Nebliger Nadelwald in kühlen Blau- und Grautönen"></div>
  <div class="heroine-art" role="img" aria-label="Illustration einer Elfenkriegerin mit Kapuze, Rüstung und Schwert"></div>
  <div class="title-band"></div>

  <div class="book-title">
    <div class="title-name">Sex auf Velora</div>
    <div class="title-sub">Anfangsgebiet</div>
  </div>

  <div class="price-panel">
    Zum<br>Einführungspreis<br>von <span class="price">-,99</span><span class="currency"> €</span>
  </div>

  <div class="sale-badge"><span>Jetzt im<br>Handel!</span></div>

  <div class="device device-tablet">
    <div class="device-screen" role="img" aria-label="Buchcover auf dem Tablet">
      <div class="cover-author">RICHARD T. HALLMOSER</div>
      <div class="cover-title">Sex auf Velora<span class="cover-sub">Anfangsgebiet</span></div>
    </div>
  </div>

  <div class="device device-phone">
    <div class="device-screen" role="img" aria-label="Buchcover auf dem Smartphone">
      <div class="cover-author">RICHARD T. HALLMOSER</div>
      <div class="cover-title">Sex auf Velora<span class="cover-sub">Anfangsgebiet</span></div>
      <div class="cover-genre">Fantasy, Erotik</div>
    </div>
  </div>

  <section class="book-pitch">
    <h1>Der neue Fantasy &amp; Erotik Roman<br>von Richard T. Hallmoser</h1>
    <p>
      <span class="line">Eines Tages kauft der Student Roman ein</span>
      <span class="line">neuartiges Online-Computerspiel und weiß</span>
      <span class="line">zu diesem Zeitpunkt noch nicht, dass sich</span>
      <span class="line">sein Sex-Leben dadurch drastisch verbes-</span>
      <span class="line-last">sern wird.</span>
    </p>
  </section>
</main>
</body>
</html>
```